Solar panel cleaning flyer design.

I'm looking for a flyer design for my new company called Brightfield Panel Works. We are a South Australian company that professionally clean residential and commercial solar panels. We generate leads by going door to door and need a flyer to hand out to our customers if they are interested in our service. As we are a new company we don't have anything particular in mind so be creative! Must include the company name and logo.

```html
<!DOCTYPE html>
<html lang="en">
<head>
<meta charset="utf-8">
<title>Brightfield Panel Works – Flyer</title>
<link rel="stylesheet" href="https://fonts.googleapis.com/css2?family=Open+Sans:wght@400;600;700;800&display=swap">
<style>
  :root {
    --blue: #1f78c8;
    --blue-deep: #155c9e;
    --green: #6cb33f;
    --green-light: #a9d86e;
    --ink: #3b3b3b;
    --body: #555b61;
    --white: #ffffff;
    --page: #e9ecef;
  }
  html, body {
    margin: 0;
    padding: 0;
    width: 900px;
    height: 1200px;
    overflow: hidden;
    background: var(--page);
    font-family: "Open Sans", Arial, sans-serif;
  }
  .flyer {
    position: relative;
    width: 900px;
    height: 1200px;
    background: var(--white);
    overflow: hidden;
  }
  .flyer-shapes { position: absolute; inset: 0; }
  .brand {
    position: absolute;
    left: 70px;
    top: 70px;
    display: flex;
    align-items: center;
    gap: 16px;
  }
  .brand-dot {
    width: 56px;
    height: 56px;
    border-radius: 50%;
    background: var(--blue);
    flex: none;
  }
  .brand-name {
    font-weight: 700;
    font-size: 30px;
    line-height: 1.1;
    color: var(--green);
    width: 220px;
  }
  .work-photo {
    position: absolute;
    width: 230px;
    height: 230px;
    border-radius: 50%;
    border: 8px solid var(--white);
    box-shadow: 0 4px 12px rgba(0,0,0,.25);
  }
  .work-photo--left {
    left: 110px; top: 240px;
    background: linear-gradient(160deg, #8ec7f0 0%, #3f74b3 55%, #25466f 100%);
  }
  .work-photo--right {
    left: 335px; top: 240px;
    background: linear-gradient(160deg, #a9d2f2 0%, #4a7fbd 50%, #b9563a 100%);
  }
  .intro {
    position: absolute;
    left: 70px;
    top: 600px;
    width: 640px;
  }
  .intro-title {
    margin: 0;
    font-size: 50px;
    font-weight: 700;
    color: var(--blue-deep);
    line-height: 1.1;
  }
  .intro-subtitle {
    margin: 4px 0 16px;
    font-size: 30px;
    font-weight: 600;
    color: var(--green);
    letter-spacing: .5px;
  }
  .intro-body {
    margin: 0;
    font-size: 19px;
    line-height: 1.45;
    color: var(--body);
  }
  .call {
    position: absolute;
    left: 110px;
    top: 870px;
  }
  .call-label {
    margin: 0 0 10px 90px;
    font-size: 40px;
    font-weight: 800;
    color: var(--ink);
  }
  .call-number {
    width: 520px;
    height: 100px;
    border-radius: 14px;
    background: linear-gradient(180deg, #2a8ad8, var(--blue-deep));
    color: var(--white);
    font-size: 58px;
    font-weight: 700;
    display: flex;
    align-items: center;
    justify-content: center;
    letter-spacing: 1px;
    box-shadow: 0 4px 10px rgba(0,0,0,.2);
  }
  .web {
    position: absolute;
    right: 60px;
    bottom: 30px;
    margin: 0;
    color: var(--white);
    font-size: 28px;
    font-weight: 700;
  }
</style>
</head>
<body>
<main class="flyer">
  <svg class="flyer-shapes" width="900" height="1200" viewBox="0 0 900 1200">
    <defs>
      <linearGradient id="roofPhoto" x1="0" y1="0" x2="0.4" y2="1">
        <stop offset="0" stop-color="#6fb6ec"/>
        <stop offset="0.35" stop-color="#b8dcf5"/>
        <stop offset="0.6" stop-color="#2f5f9c"/>
        <stop offset="1" stop-color="#1d3a63"/>
      </linearGradient>
      <linearGradient id="grassPhoto" x1="0" y1="0" x2="0" y2="1">
        <stop offset="0" stop-color="#8fcf55"/>
        <stop offset="1" stop-color="#3f8f2a"/>
      </linearGradient>
      <linearGradient id="greenSweep" x1="0" y1="0" x2="1" y2="1">
        <stop offset="0" stop-color="#cde9a6"/>
        <stop offset="1" stop-color="#6cb33f"/>
      </linearGradient>
    </defs>
    <path role="img" aria-label="Photo of a tiled roof covered with solar panels under a blue sky"
          d="M330 0 H900 V430 C650 530 320 555 0 530 V230 C170 220 280 160 330 0 Z"
          fill="url(#roofPhoto)"/>
    <path d="M0 525 C320 550 650 525 900 425 V465 C650 565 320 590 0 565 Z" fill="#1f78c8"/>
    <path d="M900 470 C770 580 760 860 900 960 Z" fill="url(#greenSweep)"/>
    <path role="img" aria-label="Photo of green grass"
          d="M900 960 C720 1050 520 1100 260 1115 L900 1100 Z" fill="url(#grassPhoto)"/>
    <path d="M0 1120 C300 1110 600 1120 900 1060 V1200 H0 Z" fill="#1f78c8"/>
    <path d="M0 1110 C300 1100 600 1110 900 1050 V1062 C600 1122 300 1114 0 1124 Z" fill="#a9d86e"/>
  </svg>

  <div class="brand">
    <span class="brand-dot"></span>
    <span class="brand-name">Brightfield Panel Works</span>
  </div>

  <div class="work-photo work-photo--left" role="img" aria-label="Photo of a worker cleaning rooftop solar panels"></div>
  <div class="work-photo work-photo--right" role="img" aria-label="Photo of a worker washing solar panels on a roof"></div>

  <section class="intro">
    <h1 class="intro-title">Lorem Ipsum is</h1>
    <p class="intro-subtitle">SIMPLY DUMMY TEXT</p>
    <p class="intro-body">Lorem Ipsum is simply dummy text of the printing and typesetting industry. Lorem Ipsum has been the industry's standard dummy text ever since the 1500s, when an unknown printer took a galley of type and scrambled it to make a type specimen book.</p>
  </section>

  <section class="call">
    <p class="call-label">CALL TODAY</p>
    <div class="call-number">088-5123-406</div>
  </section>

  <p class="web">www.brightfieldpanels.com</p>
</main>
</body>
</html>
```